Modern/Bold/Unique Prenatal Vitamin label redesign

We are in need of a design update for our Prenatal Vitamin label. We want to modernize our label and give it a fresh feel.
It should bring a feeling of fun, joy, and sophistication, but also be bold/edgy/unique and portray Trust and Authority. Our buyers are mainly mothers in the age range of 25-34 who are pregnant or breastfeeding.
I will attach our current label design, as well as some inspiration to go off of.
We like the idea of having a clean, easy to read label label with bold/vibrant colors and fonts. We like the idea of having some retro vibes in it as well
Please see the attached artwork for design inspiration (New Design Idea). We like the idea of having a pregnant mother image like the attachment on the label, with the rest of the label being white. Please come up with a unique drawing/image for the design. We cannot use a copied image or stock image.
We look forward to working with you!

```html
<!DOCTYPE html>
<html lang="en">
<head>
<meta charset="utf-8">
<title>Nola's Prenatal Glow Label</title>
<link rel="stylesheet" href="https://fonts.googleapis.com/css2?family=Poppins:wght@600&family=Roboto+Condensed:wght@500;700&family=Montserrat:wght@500;700&display=swap">
<style>
  :root {
    --pink: #e8297e;
    --pink-deep: #c2185b;
    --teal: #23a99c;
    --teal-light: #4fd1c5;
    --white: #ffffff;
    --page: #f2f2f2;
    --label-edge: #e3e3e3;
  }
  * { margin: 0; padding: 0; box-sizing: border-box; }
  html, body { width: 964px; height: 1200px; overflow: hidden; background: var(--page); }
  .canvas { position: relative; width: 964px; height: 1200px; }
  .label {
    position: absolute; left: 222px; top: 300px; width: 520px; height: 680px;
    background: var(--white); border: 1px solid var(--label-edge); overflow: hidden;
  }
  .brand {
    position: absolute; left: 46px; top: 70px;
    font-family: "Poppins", sans-serif; font-weight: 600; font-size: 112px;
    line-height: 1; letter-spacing: -3px; color: var(--pink);
  }
  .product-name {
    position: absolute; left: 48px; top: 206px;
    font-family: "Roboto Condensed", sans-serif; font-weight: 700; font-size: 62px;
    line-height: 60px; color: var(--pink);
  }
  .trust-badges { position: absolute; left: 50px; top: 384px; display: flex; gap: 16px; }
  .trust-badges span {
    width: 48px; height: 48px; border-radius: 50%;
    border: 3px solid var(--teal); background: var(--white);
    box-shadow: inset 0 0 0 7px var(--white), inset 0 0 0 30px var(--teal);
  }
  .info-band {
    position: absolute; left: 0; top: 445px; width: 520px; height: 165px;
    background: var(--pink);
  }
  .tagline {
    position: absolute; left: 48px; top: 18px;
    font-family: "Roboto Condensed", sans-serif; color: var(--white);
  }
  .tagline .lead { font-weight: 500; font-size: 26px; line-height: 28px; }
  .tagline .audience { font-weight: 700; font-size: 36px; line-height: 42px; letter-spacing: -0.5px; }
  .supplement {
    position: absolute; left: 48px; top: 130px;
    font-family: "Montserrat", sans-serif; font-weight: 500; font-size: 16px;
    letter-spacing: 0.5px; color: var(--white);
  }
  .mother-art {
    position: absolute; left: 266px; top: 230px; width: 210px; height: 380px;
    border-radius: 100px 100px 0 0;
    background: linear-gradient(160deg, var(--pink) 0%, #b83a8e 40%, var(--teal) 62%, var(--teal-light) 100%);
  }
  .count-badge {
    position: absolute; left: 378px; top: 482px; width: 94px; height: 94px;
    border-radius: 50%; border: 3px solid var(--white); background: var(--pink);
    display: flex; flex-direction: column; align-items: center; justify-content: center;
    color: var(--white); font-family: "Montserrat", sans-serif; text-align: center;
  }
  .count-badge .kind, .count-badge .unit { font-weight: 700; font-size: 10px; letter-spacing: 1px; }
  .count-badge .count { font-weight: 700; font-size: 40px; line-height: 40px; }
</style>
</head>
<body>
<main class="canvas">
  <section class="label">
    <div class="brand">Nola's</div>
    <h1 class="product-name">Prenatal<br>Glow</h1>
    <div class="trust-badges" aria-hidden="true"><span></span><span></span><span></span></div>
    <div class="info-band">
      <div class="tagline">
        <div class="lead">Premium</div>
        <div class="lead">Multivitamin for</div>
        <div class="audience">Mama &amp; Baby</div>
      </div>
      <div class="supplement">DIETARY SUPPLEMENT</div>
    </div>
    <div class="mother-art" role="img" aria-label="Illustration of a pregnant mother in profile with long flowing pink hair and a teal dress with hearts"></div>
    <div class="count-badge">
      <span class="kind">VEGGIE</span>
      <span class="count">90</span>
      <span class="unit">CAPSULES</span>
    </div>
  </section>
</main>
</body>
</html>
```